Business Card Project

We are a small consulting firm. You can experiment with any design.
Must have:
1) Company name - OLUNDEX International
2) Company slogan - simple solutions for complex problems
3) Name/Title/Phone/Email/WWW/ - use anything you like as an example.

Industry/Entity Type

Business

```html
<!DOCTYPE html>
<html lang="en">
<head>
<meta charset="utf-8">
<title>OLUNDEX International – Business Card</title>
<link rel="stylesheet" href="https://fonts.googleapis.com/css2?family=Poiret+One&display=swap">
<style>
  :root {
    --card-bg-dark: #040806;
    --card-bg-mid: #0a1711;
    --card-bg-tile: #12291d;
    --text-light: #f4f4f4;
    --text-soft: #cfd8d2;
    --logo-fill: #e0e0e0;
    --logo-ring: #3b3b3b;
    --logo-text: #1a1a1a;
    --icon-red: #e8292c;
  }
  * { margin: 0; padding: 0; box-sizing: border-box; }
  html, body {
    width: 1200px;
    height: 741px;
    overflow: hidden;
    background: var(--card-bg-dark);
  }
  .card {
    position: relative;
    width: 1200px;
    height: 741px;
    overflow: hidden;
    font-family: "Poiret One", "Century Gothic", sans-serif;
    color: var(--text-light);
  }
  .card__backdrop {
    position: absolute;
    inset: 0;
    background:
      radial-gradient(ellipse at 20% 15%, var(--card-bg-tile) 0%, transparent 50%),
      radial-gradient(ellipse at 85% 90%, var(--card-bg-tile) 0%, transparent 45%),
      linear-gradient(160deg, var(--card-bg-mid) 0%, var(--card-bg-dark) 60%, var(--card-bg-mid) 100%);
  }
  .logo-badge {
    position: absolute;
    left: 82px;
    top: 198px;
    width: 300px;
    height: 300px;
    padding-top: 12px;
    border-radius: 50%;
    background: var(--logo-fill);
    border: 6px solid var(--logo-ring);
    display: flex;
    flex-direction: column;
    align-items: center;
    justify-content: center;
    color: var(--logo-text);
    font-size: 50px;
    line-height: 62px;
    letter-spacing: 6px;
    text-align: center;
  }
  .person {
    position: absolute;
    left: 82px;
    top: 522px;
    width: 300px;
    text-align: center;
  }
  .person__name {
    font-size: 32px;
    line-height: 40px;
    letter-spacing: 1.5px;
    font-weight: 400;
  }
  .person__title {
    font-size: 22px;
    line-height: 30px;
    letter-spacing: 2px;
    color: var(--text-soft);
  }
  .company {
    position: absolute;
    left: 495px;
    top: 215px;
  }
  .company__name {
    font-size: 59px;
    font-weight: 400;
    letter-spacing: 3.5px;
    line-height: 66px;
    white-space: nowrap;
  }
  .company__slogan {
    font-size: 30px;
    letter-spacing: 4.5px;
    line-height: 32px;
    margin-left: 2px;
    white-space: nowrap;
  }
  .contact {
    position: absolute;
    left: 495px;
    top: 384px;
    list-style: none;
    font-size: 46px;
    letter-spacing: 1.5px;
    line-height: 55px;
  }
  .contact__item {
    display: flex;
    align-items: flex-start;
    white-space: nowrap;
  }
  .contact__icon {
    width: 44px;
    height: 55px;
    flex: 0 0 44px;
    fill: var(--icon-red);
  }
  .contact__text { padding-left: 4px; }
</style>
</head>
<body>
  <main class="card">
    <div class="card__backdrop" role="img" aria-label="Dark background with a scattered mosaic of small green tiles"></div>

    <div class="logo-badge">
      <span>LOGO</span>
      <span>HERE</span>
    </div>

    <div class="person">
      <p class="person__name">Alya Rahman</p>
      <p class="person__title">Senior Consultant</p>
    </div>

    <header class="company">
      <h1 class="company__name">OLUNDEX International</h1>
      <p class="company__slogan">simple solutions for complex problems</p>
    </header>

    <ul class="contact">
      <li class="contact__item">
        <svg class="contact__icon" viewBox="0 0 44 54" aria-hidden="true">
          <path d="M12 12c2-1 4-1 5 1l3 6c1 2 0 3-1 4l-2 2c2 5 6 9 11 11l2-2c1-1 2-2 4-1l6 3c2 1 2 3 1 5l-2 3c-2 2-5 2-8 1C19 40 9 30 5 18c-1-3 0-5 2-7z"/>
        </svg>
        <span class="contact__text">0.1.0.7.3.6.1.8.4.2</span>
      </li>
      <li class="contact__item">
        <svg class="contact__icon" viewBox="0 0 44 54" aria-hidden="true">
          <path d="M3 14h38v26H3z"/>
          <path d="M5 16l17 13 17-13M5 38l13-11M39 38L26 27" fill="none" stroke="#0a0f0c" stroke-width="2.5"/>
        </svg>
        <span class="contact__text">hello@olundex.example</span>
      </li>
      <li class="contact__item">
        <svg class="contact__icon" viewBox="0 0 44 54" aria-hidden="true">
          <path d="M22 10c-8 0-14 6-14 14 0 10 14 24 14 24s14-14 14-24c0-8-6-14-14-14zm0 19a5 5 0 1 1 0-10 5 5 0 0 1 0 10z"/>
        </svg>
        <span class="contact__text">No 12 Jalan Meranti Indah,<br>50480 Taman Seri.</span>
      </li>
      <li class="contact__item">
        <svg class="contact__icon" viewBox="0 0 44 54" aria-hidden="true">
          <g fill="none" stroke="var(--icon-red)" stroke-width="3">
            <circle cx="22" cy="28" r="15"/>
            <ellipse cx="22" cy="28" rx="6.5" ry="15"/>
            <path d="M7 28h30M10 20h24M10 36h24"/>
          </g>
        </svg>
        <span class="contact__text">www.olundex.example</span>
      </li>
    </ul>
  </main>
</body>
</html>
```